VFX Company Business Card Design Project

The Pixel Harbor is a decentralized Visual Effects Studio servicing the television and feature film industries.
Project Brief:
Take our logo that was previously designed on Sketch Forum and make a double sided business card.
Requirements:
- Card MUST be double sided.
- Front of card MUST have the yellow part of our logo against the dark grey background.
- Back of card is completely up to the designer.
- Back of card must include the complete company logo.
Please follow these File Preparation guidelines:
http://printmarlow.example/infopage?file=filetype_en&s=PrintMarlow_new&lang=en
Industry/Entity Type
Business
Look and feel
Each slider illustrates characteristics of the customer's brand and the style your logo design should communicate.

```html
<!DOCTYPE html>
<html lang="en">
<head>
<meta charset="utf-8">
<title>The Pixel Harbor – Business Card</title>
<link rel="stylesheet" href="https://fonts.googleapis.com/css2?family=Asap:wght@400;500&display=swap">
<style>
  :root {
    --page: #e6e8ea;
    --card: #3a3a3a;
    --card-front: #363636;
    --text: #f2f2f2;
    --muted: #d6d6d6;
    --rule: #bdbdbd;
    --accent: #f5c51c;
  }
  * { box-sizing: border-box; margin: 0; padding: 0; }
  html, body {
    width: 1200px; height: 960px; overflow: hidden;
    background: var(--page);
    font-family: "Asap", sans-serif;
  }
  .sheet {
    width: 1200px; height: 960px;
    display: flex; flex-direction: column; align-items: center; justify-content: center;
    gap: 60px;
  }
  .card {
    position: relative;
    width: 700px; height: 400px;
    background: var(--card);
    box-shadow: 0 10px 30px rgba(0,0,0,.25);
    color: var(--text);
  }
  /* Contact side */
  .card--contact .brand {
    position: absolute; top: 52px; right: 50px;
    display: flex; align-items: center; gap: 12px;
    color: var(--accent); font-size: 34px; font-weight: 500;
  }
  .brand-dot { width: 22px; height: 22px; border-radius: 50%; background: var(--accent); }
  .holder { position: absolute; left: 40px; top: 196px; }
  .holder-name { font-size: 32px; font-weight: 400; letter-spacing: .5px; }
  .holder-role { font-size: 17px; color: var(--muted); margin-top: 6px; }
  .divider {
    position: absolute; left: 40px; right: 40px; top: 272px;
    border-top: 1.5px solid var(--rule);
  }
  .contacts {
    position: absolute; left: 40px; top: 298px;
    list-style: none; font-size: 19px; line-height: 29px;
  }
  .contacts li { display: flex; gap: 22px; }
  .contacts .label { color: var(--accent); width: 12px; }
  .address {
    position: absolute; left: 372px; top: 290px;
    font-size: 16px; line-height: 24px; font-style: normal; color: var(--muted);
  }
  /* Logo side */
  .card--logo {
    background: var(--card-front);
    display: flex; align-items: center; justify-content: center;
  }
  .card--logo .brand {
    display: flex; align-items: center; gap: 16px;
    color: var(--accent); font-size: 48px; font-weight: 500;
  }
  .card--logo .brand-dot { width: 30px; height: 30px; }
</style>
</head>
<body>
<main class="sheet">
  <section class="card card--contact" aria-label="Business card, contact side">
    <div class="brand"><span class="brand-dot"></span><span>The Pixel Harbor</span></div>
    <div class="holder">
      <h1 class="holder-name">ALEX MORROW</h1>
      <p class="holder-role">Managing Partner</p>
    </div>
    <hr class="divider">
    <ul class="contacts">
      <li><span class="label">t</span><span>(480) 555-0142</span></li>
      <li><span class="label">e</span><span>name@pixelharbor.example</span></li>
      <li><span class="label">w</span><span>www.pixelharbor.example</span></li>
    </ul>
    <address class="address">4410 Harbor View Road,<br>Suite 210, Lakeport,<br>Oregon 97000</address>
  </section>

  <section class="card card--logo" aria-label="Business card, logo side">
    <div class="brand"><span class="brand-dot"></span><span>The Pixel Harbor</span></div>
  </section>
</main>
</body>
</html>
```